Professional Trustee Company - Business Cards
Thornwick Crest Fiduciary Services, Inc.
Designers:
(1) Please be sure that the logo is large enough to be easily read as in some cases it appears like the words are too small to read.
(2) Please have the back of the card read: Earning your trust is our business.
RT/KPH/WN Team
Please note that I am also looking for stationary and envelope designs in black and white only. Thank you!

```html
<!DOCTYPE html>
<html lang="en">
<head>
<meta charset="utf-8">
<title>Thornwick Crest Fiduciary Services, Inc. – Business Cards</title>
<link rel="stylesheet" href="https://fonts.googleapis.com/css2?family=Cinzel:wght@600&family=Lato:wght@400;700&display=swap">
<style>
  :root{
    --bg:#e8e5e0;
    --card:#ffffff;
    --ink:#3a3a3a;
    --ink-soft:#777777;
    --rule:#cfcfcf;
    --band-dark:#4a4a4a;
    --band-light:#8a8a8a;
    --mark:#5a5a5a;
  }
  *{box-sizing:border-box;margin:0;padding:0}
  html,body{width:1200px;height:629px;overflow:hidden;background:var(--bg)}
  body{position:relative;font-family:"Lato",sans-serif;color:var(--ink)}
  .card{
    position:absolute;top:150px;width:520px;height:300px;background:var(--card);
    box-shadow:0 6px 18px rgba(0,0,0,.18);overflow:hidden;
  }
  .card--back{left:50px}
  .card--front{left:630px}

  .brand{position:absolute;display:flex;align-items:center;gap:16px}
  .card--back .brand{left:70px;top:92px}
  .card--front .brand{left:46px;top:40px}
  .brand__disc{width:78px;height:78px;border-radius:50%;background:var(--mark);flex:none}
  .brand__name{font-family:"Cinzel",serif;font-weight:600;color:var(--ink);line-height:1.05}
  .brand__name .lead{display:block;font-size:34px;letter-spacing:3px}
  .brand__name .sub{display:block;font-size:15px;letter-spacing:1.6px;margin-top:4px}
  .brand__tagline{display:block;font-family:"Lato",sans-serif;font-size:9px;letter-spacing:1.5px;color:var(--ink-soft);margin-top:6px;text-transform:uppercase}

  .holder{position:absolute;left:46px;top:158px;font-size:10px;line-height:1.55;color:var(--ink)}
  .holder__name{font-weight:700;font-size:11px}
  .holder__title{color:var(--ink-soft);margin-bottom:6px}

  .contacts{position:absolute;left:300px;top:150px;border-left:1px solid var(--rule);padding-left:16px;list-style:none}
  .contacts li{display:flex;align-items:center;gap:8px;font-size:10px;height:19px}
  .contacts svg{width:13px;height:13px;flex:none}

  .band{
    position:absolute;left:0;right:0;bottom:0;height:38px;
    background:linear-gradient(90deg,var(--band-light),var(--band-dark));
    color:#fff;font-size:11px;letter-spacing:3px;display:flex;align-items:center;justify-content:flex-end;padding-right:30px;
  }
</style>
</head>
<body>
  <section class="card card--back">
    <div class="brand">
      <span class="brand__disc"></span>
      <p class="brand__name">
        <span class="lead">THORNWICK CREST</span>
        <span class="sub">FIDUCIARY SERVICES</span>
        <span class="brand__tagline">Earning your trust is our business</span>
      </p>
    </div>
  </section>

  <section class="card card--front">
    <div class="brand">
      <span class="brand__disc"></span>
      <p class="brand__name">
        <span class="lead">THORNWICK CREST</span>
        <span class="sub">FIDUCIARY SERVICES</span>
        <span class="brand__tagline">Earning your trust is our business</span>
      </p>
    </div>

    <div class="holder">
      <p class="holder__name">Renata Thorne, CPA</p>
      <p class="holder__title">Licensed Fiduciary</p>
      <p>120 Harbor Lane, Suite 4</p>
      <p>Easton, CA 90210</p>
    </div>

    <ul class="contacts">
      <li><svg viewBox="0 0 14 14"><circle cx="7" cy="7" r="7" fill="#4a4a4a"/><path d="M4.5 4h1.6l.6 1.7-.9.7a4 4 0 0 0 1.8 1.8l.7-.9 1.7.6V9.5A1 1 0 0 1 9 10.5 6 6 0 0 1 3.5 5a1 1 0 0 1 1-1z" fill="#fff"/></svg>(555) 014-2280</li>
      <li><svg viewBox="0 0 14 14"><circle cx="7" cy="7" r="7" fill="#4a4a4a"/><rect x="4" y="5" width="6" height="5" fill="#fff"/><rect x="5" y="3.5" width="4" height="2" fill="#fff"/></svg>(555) 014-2291</li>
      <li><svg viewBox="0 0 14 14"><circle cx="7" cy="7" r="7" fill="#4a4a4a"/><rect x="3.5" y="4.5" width="7" height="5" fill="none" stroke="#fff"/><path d="M3.5 4.5 7 7.5l3.5-3" fill="none" stroke="#fff"/></svg>info@thornwickcrest.com</li>
      <li><svg viewBox="0 0 14 14"><circle cx="7" cy="7" r="7" fill="#4a4a4a"/><circle cx="7" cy="7" r="3.5" fill="none" stroke="#fff"/><path d="M3.5 7h7M7 3.5v7" stroke="#fff"/></svg>www.thornwickcrest.com</li>
    </ul>

    <div class="band">www.thornwickcrest.com</div>
  </section>
</body>
</html>
```